Business Card Design

We are a commercial real estate brokerage in San Francisco, leasing office buildings downtown.
I would like a clean, elegant look. Simple but powerful .

Industry/Entity Type

Business

Contact Information for Business Card

Derek Hollings
lic# 02875140
415.287.6041
derek@vexa-commercial.com
vexa-commercial.com

```html
<!DOCTYPE html>
<html lang="en">
<head>
<meta charset="utf-8">
<title>VEXA Commercial — Business Cards</title>
<link rel="stylesheet" href="https://fonts.googleapis.com/css2?family=Arimo:wght@400;700&display=swap">
<style>
  :root {
    --backdrop: #3a312c;
    --card: #151515;
    --card-edge: #1d1d1d;
    --brand: #7482a0;
    --name: #8391b0;
    --ink: #d9dce2;
    --ink-soft: #c4c7cd;
    --rule: #3a3d44;
  }
  * { margin: 0; padding: 0; box-sizing: border-box; }
  html, body {
    width: 1200px;
    height: 787px;
    overflow: hidden;
    background: var(--backdrop);
    font-family: "Arimo", Arial, sans-serif;
  }
  .sheet {
    width: 1200px;
    height: 787px;
    display: flex;
    align-items: center;
    justify-content: center;
    gap: 44px;
  }
  .card {
    position: relative;
    width: 540px;
    height: 309px;
    background: var(--card);
    border: 1px solid var(--card-edge);
    box-shadow: 0 14px 30px rgba(0,0,0,.45);
  }
  .brand {
    display: flex;
    align-items: center;
    gap: 14px;
  }
  .brand-mark {
    width: 22px;
    height: 22px;
    background: var(--brand);
  }
  .brand-name {
    color: var(--brand);
    font-weight: 700;
    font-size: 30px;
    letter-spacing: 1px;
    line-height: 1;
  }
  /* reverse side */
  .card-back .brand {
    position: absolute;
    left: 70px;
    top: 78px;
  }
  .tagline {
    position: absolute;
    left: 70px;
    top: 150px;
    width: 400px;
    color: var(--ink-soft);
    font-size: 15px;
    line-height: 1.45;
  }
  /* contact side */
  .card-front .brand {
    position: absolute;
    left: 42px;
    top: 72px;
  }
  .card-front .brand-name { font-size: 26px; }
  .contact {
    position: absolute;
    left: 300px;
    top: 140px;
    color: var(--ink);
    font-size: 16px;
  }
  .contact-name {
    color: var(--name);
    font-size: 20px;
    letter-spacing: .5px;
    margin-bottom: 10px;
  }
  .contact-line {
    display: flex;
    align-items: center;
    gap: 8px;
    height: 23px;
  }
  .contact-line .icon { width: 14px; height: 14px; fill: var(--ink); flex: none; }
  .contact-line .pad { width: 14px; flex: none; }
</style>
</head>
<body>
<main class="sheet">
  <section class="card card-back">
    <div class="brand">
      <span class="brand-mark"></span>
      <span class="brand-name">VEXA Commercial</span>
    </div>
    <p class="tagline">commercial real estate brokerage in San Francisco leasing office buildings downtown.</p>
  </section>

  <section class="card card-front">
    <div class="brand">
      <span class="brand-mark"></span>
      <span class="brand-name">VEXA Commercial</span>
    </div>
    <div class="contact">
      <p class="contact-name">Derek Hollings</p>
      <p class="contact-line"><span>lic# 02875140</span></p>
      <p class="contact-line">
        <svg class="icon" viewBox="0 0 16 16" aria-hidden="true"><path d="M3 1h3l1.5 4-2 1.3a9 9 0 0 0 4.2 4.2L11 8.5l4 1.5v3a2 2 0 0 1-2 2A12 12 0 0 1 1 3a2 2 0 0 1 2-2z"/></svg>
        <span>415.287.6041</span>
      </p>
      <p class="contact-line">
        <svg class="icon" viewBox="0 0 16 16" aria-hidden="true"><path d="M1 3h14v10H1z M1 3l7 6 7-6" fill="none" stroke="#d9dce2" stroke-width="1.6"/></svg>
        <span>derek@vexa-commercial.com</span>
      </p>
      <p class="contact-line">
        <svg class="icon" viewBox="0 0 16 16" aria-hidden="true"><path d="M8 1a5 5 0 0 0-5 5c0 4 5 9 5 9s5-5 5-9a5 5 0 0 0-5-5zm0 7a2 2 0 1 1 0-4 2 2 0 0 1 0 4z"/></svg>
        <span>vexa-commercial.com</span>
      </p>
    </div>
  </section>
</main>
</body>
</html>
```